Flyer Designer for a Widow and Door Company - loooking for fresh design

We are looking for a flyer designed to advertise our business - we supply and install windows and doors - we are looking for a fresh looking flyer to distribute to drum up business - more information can be found at our website www.brightpanehouse.co.uk - We want a different approach than we currently have - making it vibrant and fresh - you can see the services on the website but its more the graphical design that we are looking for rather than content as the content from the website can be used for each service etc.

Target Market(s)

the general public

Colors

Designer to choose colors to be used in the design.

Requirements
Must have
• vibrant design and images

```html
<!DOCTYPE html>
<html lang="en">
<head>
<meta charset="utf-8">
<title>Brightpane House Ltd – Flyer</title>
<link rel="stylesheet" href="https://fonts.googleapis.com/css2?family=Bebas+Neue&family=Montserrat:wght@400;500;700;800&display=swap">
<style>
  :root {
    --backdrop: #3b3e43;
    --navy: #0d1a8c;
    --royal: #1b2aa8;
    --sky: #2f7fd6;
    --ink: #2a2a2e;
    --body-bg: #eef3f9;
    --card: #ffffff;
    --footer-dark: #16181c;
    --silver-1: #f2f2f2;
    --silver-2: #bdbdbd;
  }
  * { margin: 0; padding: 0; box-sizing: border-box; }
  html, body { width: 1200px; height: 1000px; overflow: hidden; }
  body { background: var(--backdrop); font-family: "Montserrat", sans-serif; }

  .flyer {
    position: absolute; left: 270px; top: 33px;
    width: 660px; height: 934px; overflow: hidden;
    background: linear-gradient(160deg, #f7f9fc 0%, var(--body-bg) 60%, #e4ebf4 100%);
    box-shadow: 0 8px 30px rgba(0,0,0,.45);
  }

  .hero-photo {
    position: absolute; left: 0; top: 0; width: 660px; height: 440px;
    background: linear-gradient(120deg, #f1f0ee 0%, #e6e4e1 45%, #cfd6de 70%, #a7917a 100%);
  }
  .roof { position: absolute; left: 0; top: 340px; width: 660px; height: 100px; }

  .brand-banner {
    position: absolute; left: 47px; top: 0; width: 206px; height: 147px;
  }
  .brand-banner svg { position: absolute; inset: 0; }
  .brand-name {
    position: absolute; left: 14px; right: 10px; top: 48px;
    display: flex; align-items: center; gap: 8px;
    font-family: "Montserrat", sans-serif; font-weight: 800;
    font-size: 17px; line-height: 1.05; color: var(--royal); text-transform: uppercase;
  }
  .brand-mark { width: 30px; height: 30px; background: var(--royal); flex: none; }

  .headline {
    position: absolute; left: 0; right: 0; top: 436px;
    display: flex; align-items: center; justify-content: center; gap: 12px;
    font-family: "Bebas Neue", sans-serif; font-size: 46px; color: var(--ink); letter-spacing: .5px;
  }
  .headline .rule { width: 60px; height: 2px; background: var(--sky); }
  .subline {
    position: absolute; left: 0; right: 0; top: 484px; text-align: center;
    font-weight: 800; font-size: 25px; color: var(--sky); letter-spacing: .3px;
  }

  .transformation {
    position: absolute; top: 548px; width: 180px; height: 125px;
    display: grid; grid-template-columns: 1fr 1fr; gap: 2px;
    background: #fff; padding: 0; box-shadow: 0 2px 6px rgba(0,0,0,.25);
  }
  .transformation.one { left: 43px; }
  .transformation.two { left: 243px; }
  .transformation.three { left: 443px; }
  .shot { position: relative; }
  .shot .photo { position: absolute; left: 0; right: 0; top: 0; bottom: 16px; }
  .shot .tag {
    position: absolute; left: 0; right: 0; bottom: 0; height: 16px;
    background: var(--sky); color: #fff; text-align: center;
    font-family: "Bebas Neue", sans-serif; font-size: 13px; line-height: 17px;
  }

  .section-title {
    position: absolute; left: 43px; right: 38px; top: 708px;
    display: flex; align-items: center; gap: 12px;
    font-weight: 700; font-size: 19px; color: var(--ink);
  }
  .section-title .rule { flex: 1; height: 2px; background: var(--sky); }

  .service { position: absolute; top: 759px; width: 108px; text-align: center; }
  .service.windows { left: 43px; }
  .service.doors { left: 198px; }
  .service.repairs { left: 353px; }
  .service.landlord { left: 508px; width: 118px; }
  .service .tile {
    width: 107px; height: 78px; background: var(--card); border-radius: 8px;
    box-shadow: 0 2px 6px rgba(20,40,90,.15);
    display: flex; align-items: center; justify-content: center; margin: 0 auto;
  }
  .service .label {
    margin-top: 15px; font-family: "Bebas Neue", sans-serif;
    font-size: 20px; color: var(--navy); white-space: nowrap;
  }

  .footer { position: absolute; left: 0; bottom: 0; width: 660px; height: 48px; background: var(--footer-dark); }
  .footer svg { position: absolute; left: 0; top: 0; }
  .quote {
    position: absolute; left: 43px; top: 8px; color: #fff; line-height: 1.1;
  }
  .quote .ask { font-size: 13px; font-weight: 500; }
  .quote .call { font-size: 16px; font-weight: 800; }
  .web {
    position: absolute; left: 296px; top: 16px; color: #fff; font-size: 11.5px;
    display: flex; align-items: center; gap: 5px;
  }
  .web .globe { width: 11px; height: 11px; border: 1.5px solid var(--sky); border-radius: 50%; }
  .divider { position: absolute; left: 496px; top: 12px; height: 24px; border-left: 1px dashed #fff; }
  .social {
    position: absolute; left: 505px; top: 15px; color: #fff; font-size: 11.5px;
    display: flex; align-items: center; gap: 7px;
  }
  .social .dot { width: 16px; height: 16px; border: 1.5px solid var(--sky); border-radius: 50%; }
</style>
</head>
<body>
<main class="flyer">
  <div class="hero-photo" role="img" aria-label="Photo of a happy family in a bright room with new white windows, father lifting a toddler"></div>

  <svg class="roof" viewBox="0 0 660 100" aria-hidden="true">
    <polygon points="0,60 330,8 660,60 660,74 330,22 0,74" fill="var(--navy)"/>
    <polygon points="0,74 330,22 660,74 660,84 330,32 0,84" fill="var(--sky)"/>
    <polygon points="0,84 330,32 660,84 660,100 0,100" fill="#f5f8fc"/>
  </svg>

  <div class="brand-banner">
    <svg viewBox="0 0 206 147" width="206" height="147" aria-hidden="true">
      <defs>
        <linearGradient id="silver" x1="0" y1="0" x2="0" y2="1">
          <stop offset="0" stop-color="var(--silver-2)"/>
          <stop offset=".6" stop-color="var(--silver-1)"/>
          <stop offset="1" stop-color="#d9d9d9"/>
        </linearGradient>
      </defs>
      <polygon points="0,0 206,0 206,147 103,125 0,147" fill="url(#silver)" stroke="#fff" stroke-width="2"/>
    </svg>
    <div class="brand-name"><span class="brand-mark"></span><span>Brightpane<br>House Ltd</span></div>
  </div>

  <h1 class="headline"><span class="rule"></span>Installers &amp; Suppliers<span class="rule"></span></h1>
  <p class="subline">OF BESPOKE WINDOWS AND DOORS</p>

  <div class="transformation one">
    <div class="shot"><div class="photo" role="img" aria-label="Front door before: dark red wooden door" style="background:linear-gradient(#d8d4cc,#4a1414 30%,#3a0e0e)"></div><span class="tag">Before</span></div>
    <div class="shot"><div class="photo" role="img" aria-label="Front door after: sage green composite door" style="background:linear-gradient(#dcd9d2,#7fb0a0 30%,#6a9a8b)"></div><span class="tag">After</span></div>
  </div>
  <div class="transformation two">
    <div class="shot"><div class="photo" role="img" aria-label="Front door before: black door with patterned glass" style="background:linear-gradient(#1a1e2a,#0d0f18)"></div><span class="tag">Before</span></div>
    <div class="shot"><div class="photo" role="img" aria-label="Front door after: dark green door with leaded glass" style="background:linear-gradient(#2d3a2e,#1a241b)"></div><span class="tag">After</span></div>
  </div>
  <div class="transformation three">
    <div class="shot"><div class="photo" role="img" aria-label="Front door before: plain white door" style="background:linear-gradient(90deg,#7a6c5c,#e8e8e6 45%,#9aa6a0)"></div><span class="tag">Before</span></div>
    <div class="shot"><div class="photo" role="img" aria-label="Front door after: anthracite grey door" style="background:linear-gradient(90deg,#2e3540,#3b4350 70%,#dfe3e6)"></div><span class="tag">After</span></div>
  </div>

  <h2 class="section-title"><span class="rule"></span>OUR SERVICES<span class="rule"></span></h2>

  <div class="service windows">
    <div class="tile">
      <svg width="36" height="56" viewBox="0 0 36 56" aria-hidden="true">
        <rect x="0" y="0" width="36" height="56" fill="var(--royal)"/>
        <g fill="#fff">
          <rect x="4" y="4" width="8" height="10"/><rect x="14" y="4" width="8" height="10"/><rect x="24" y="4" width="8" height="10"/>
          <rect x="4" y="16" width="8" height="10"/><rect x="14" y="16" width="8" height="10"/><rect x="24" y="16" width="8" height="10"/>
          <rect x="4" y="30" width="8" height="10"/><rect x="14" y="30" width="8" height="10"/><rect x="24" y="30" width="8" height="10"/>
          <rect x="4" y="42" width="8" height="10"/><rect x="14" y="42" width="8" height="10"/><rect x="24" y="42" width="8" height="10"/>
        </g>
      </svg>
    </div>
    <p class="label">OUR WINDOWS</p>
  </div>
  <div class="service doors">
    <div class="tile">
      <svg width="36" height="58" viewBox="0 0 36 58" aria-hidden="true">
        <path d="M2 2 H34 V54 H30 V6 H6 V54 H2 Z" fill="var(--royal)"/>
        <path d="M6 8 L24 2 V56 L6 52 Z" fill="var(--royal)"/>
        <circle cx="20" cy="30" r="1.8" fill="#fff"/>
      </svg>
    </div>
    <p class="label">OUR DOORS</p>
  </div>
  <div class="service repairs">
    <div class="tile">
      <svg width="48" height="48" viewBox="0 0 48 48" aria-hidden="true">
        <g fill="var(--royal)">
          <rect x="20" y="-4" width="8" height="46" rx="3" transform="rotate(45 24 24)"/>
          <rect x="21" y="4" width="6" height="38" rx="2" transform="rotate(-45 24 24)"/>
          <circle cx="39" cy="9" r="8"/>
          <circle cx="9" cy="39" r="5"/>
        </g>
        <circle cx="42" cy="6" r="4" fill="#fff"/>
      </svg>
    </div>
    <p class="label">REPAIRS</p>
  </div>
  <div class="service landlord">
    <div class="tile">
      <svg width="56" height="48" viewBox="0 0 56 48" aria-hidden="true">
        <path d="M2 18 L28 2 L54 18 V36 H18 L6 46 L10 36 H2 Z" fill="var(--royal)"/>
      </svg>
    </div>
    <p class="label">LANDLORD SERVICES</p>
  </div>

  <footer class="footer">
    <svg width="660" height="48" viewBox="0 0 660 48" aria-hidden="true">
      <polygon points="0,0 246,0 280,24 246,48 0,48" fill="var(--navy)"/>
      <polygon points="246,0 258,0 292,24 258,48 246,48 280,24" fill="var(--sky)"/>
    </svg>
    <div class="quote"><p class="ask">REQUEST A FREE QUOTE</p><p class="call">CALL 01632 960418</p></div>
    <p class="web"><span class="globe"></span>www.brightpanehouse.co.uk</p>
    <span class="divider"></span>
    <p class="social">follow us: <span class="dot"></span><span class="dot"></span><span class="dot"></span></p>
  </footer>
</main>
</body>
</html>
```